Varn Spark Solutions requires a modern & sharp looking sign.

We need a sign to be designed for a local soccer club ground where advertising will take place. Text needs to be limited with only the basic information such as the logo/company name, website and mobile number. The EC40392 number must be placed somewhere in the sign.

The design should be similar to the flyer design attached, but in a more plain looking version.

Signage dimensions are 2050mm Wide x 900mm High.

Industry/Entity Type

Electrician

Requirements
Must have
• Logo/Company Name
• EC Number
• Website (www.varnspark.com.au)
• Phone Number
• - SAME COLOR SCHEME AS THE LOGO
• - SAME LIGHTNING BOLT TO THE RIGHT OF THE SIGN (REFER TO FLYER)
Should not have
• NO PICTURES

```html
<!DOCTYPE html>
<html lang="en">
<head>
<meta charset="utf-8">
<title>Varn Spark Solutions – Ground Sign</title>
<link rel="stylesheet" href="https://fonts.googleapis.com/css2?family=Michroma&family=Roboto:wght@500;700;900&display=swap">
<style>
  :root {
    --brand-blue: #454f9d;
    --brand-grey: #9c9d9e;
    --ring-grey: #d9dadb;
    --paper-light: #ffffff;
    --paper-shade: #e4e5e6;
    --ink-white: #ffffff;
  }
  html, body {
    margin: 0;
    padding: 0;
    overflow: hidden;
    background: #ffffff;
  }
  .sign {
    position: relative;
    width: 1200px;
    height: 527px;
    overflow: hidden;
    background: linear-gradient(135deg, var(--paper-light) 0%, var(--paper-light) 35%, var(--paper-shade) 100%);
  }
  .sign__disc {
    position: absolute;
    left: 640px;
    top: -32px;
    width: 592px;
    height: 592px;
    border-radius: 50%;
    background: var(--brand-grey);
    box-shadow: 0 0 0 22px var(--ring-grey);
  }
  .brand-name {
    position: absolute;
    left: 48px;
    top: 40px;
    margin: 0;
    font-family: "Michroma", sans-serif;
    font-weight: 400;
    color: var(--brand-blue);
    line-height: 1;
  }
  .brand-name__main {
    display: block;
    font-size: 78px;
    letter-spacing: 2px;
  }
  .brand-name__sub {
    display: block;
    margin-top: 44px;
    font-size: 46px;
    letter-spacing: 12px;
  }
  .phone-band {
    position: absolute;
    left: 0;
    top: 324px;
    width: 656px;
    height: 96px;
    background: var(--brand-blue);
    clip-path: polygon(0 0, 624px 0, 656px 100%, 0 100%);
    display: flex;
    align-items: center;
  }
  .phone-band__text {
    margin: 0 0 0 50px;
    font-family: "Roboto", sans-serif;
    font-weight: 700;
    font-size: 58px;
    color: var(--ink-white);
    letter-spacing: 1px;
  }
  .website {
    position: absolute;
    left: 50px;
    top: 446px;
    margin: 0;
    font-family: "Roboto", sans-serif;
    font-weight: 700;
    font-size: 44px;
    color: var(--brand-blue);
  }
  .licence {
    position: absolute;
    left: 984px;
    top: 452px;
    margin: 0;
    font-family: "Roboto", sans-serif;
    font-weight: 900;
    font-size: 34px;
    color: var(--ink-white);
    letter-spacing: 1px;
    text-shadow:
      2px 0 0 var(--brand-blue), -2px 0 0 var(--brand-blue),
      0 2px 0 var(--brand-blue), 0 -2px 0 var(--brand-blue),
      2px 2px 0 var(--brand-blue), -2px -2px 0 var(--brand-blue),
      2px -2px 0 var(--brand-blue), -2px 2px 0 var(--brand-blue);
  }
</style>
</head>
<body>
  <div class="sign">
    <div class="sign__disc" aria-hidden="true"></div>

    <h1 class="brand-name">
      <span class="brand-name__main">VARN SPARK</span>
      <span class="brand-name__sub">SOLUTIONS</span>
    </h1>

    <div class="phone-band">
      <p class="phone-band__text">Tel 0400 555 193</p>
    </div>

    <p class="website">www.varnspark.com.au</p>

    <p class="licence">EC40392</p>
  </div>
</body>
</html>
```